International Wine Label 202001

Need a wine label designed for several new wines from California being exported to Asia. This label should be focused around an animal theme of the flowing: Tiger, Lion, Horse or Eagle. The label should be adaptable to a product line of wines. For example the label could be used for a Cabernet wine, Merlot, Chardonnay or Pinot. A slight modification to the label design should be incorporated to allow for the different varietals. Front label design only. Can utilize photo image in design.
The label would be around 5.75" x 3.50".

Target Market(s)

25-35 year old wine buyers in the global market

Industry/Entity Type

Retail

Font styles to use
Sans Serif

Requirements
Must have
• Wine name based on design (designer suggest name)
Wine varietals
Vintage date
Additional wording area
Nice to have
• Rectangular label preferred Front label only.

```html
<!DOCTYPE html>
<html lang="en">
<head>
<meta charset="utf-8">
<title>Open Range – Cabernet Sauvignon Label</title>
<link rel="stylesheet" href="https://fonts.googleapis.com/css2?family=Cormorant+Garamond:wght@500;600&display=swap">
<style>
  :root {
    --backdrop: #bdbdbd;
    --label-black: #1c1c1c;
    --label-edge: #141414;
    --silver: #c9c9c9;
    --silver-soft: #a9a9a9;
    --art-light: #6a6a6a;
    --art-dark: #1c1c1c;
  }
  * { margin: 0; padding: 0; box-sizing: border-box; }
  html, body {
    width: 1200px;
    height: 960px;
    overflow: hidden;
    background: var(--backdrop);
  }
  .canvas {
    position: relative;
    width: 1200px;
    height: 960px;
  }
  .wine-label {
    position: absolute;
    left: 320px;
    top: 160px;
    width: 560px;
    height: 640px;
    background: var(--label-black);
    border: 1px solid var(--label-edge);
    overflow: hidden;
    font-family: "Cormorant Garamond", Georgia, serif;
    color: var(--silver);
  }
  .wine-name {
    position: absolute;
    left: 56px;
    top: 64px;
    font-weight: 600;
    font-size: 104px;
    line-height: 0.92;
    letter-spacing: 1px;
    color: var(--silver);
  }
  .wine-name span { display: block; }
  .wine-name .second-line { padding-left: 36px; }
  .lion-art {
    position: absolute;
    right: 0;
    top: 170px;
    width: 330px;
    height: 340px;
    background: radial-gradient(ellipse at 70% 40%, var(--art-light) 0%, #3a3a3a 45%, var(--art-dark) 80%);
    opacity: 0.85;
  }
  .varietal-block {
    position: absolute;
    left: 0;
    right: 0;
    bottom: 48px;
    text-align: center;
  }
  .varietal {
    font-weight: 500;
    font-size: 40px;
    letter-spacing: 2px;
    color: var(--silver);
  }
  .varietal-rule {
    width: 372px;
    height: 2px;
    margin: 12px auto 14px;
    background: var(--silver-soft);
  }
  .region {
    font-weight: 500;
    font-size: 28px;
    letter-spacing: 2px;
    color: var(--silver-soft);
  }
  .vintage {
    margin-top: 6px;
    font-weight: 500;
    font-size: 28px;
    letter-spacing: 2px;
    color: var(--silver-soft);
  }
</style>
</head>
<body>
  <main class="canvas">
    <section class="wine-label">
      <div class="lion-art" role="img" aria-label="Engraved-style illustration of a lion's head in silver on black, gazing upward"></div>
      <h1 class="wine-name">
        <span class="first-line">Open</span>
        <span class="second-line">Range</span>
      </h1>
      <div class="varietal-block">
        <p class="varietal">CABERNET SAUVIGNON</p>
        <div class="varietal-rule"></div>
        <p class="region">NAPA VALLEY</p>
        <p class="vintage">2015</p>
      </div>
    </section>
  </main>
</body>
</html>
```